Modern Label for cleaning products for the brand Voralux

We need a label design for our line of cleaning products. The label should feature our logo and an image to identify the product's intended use. I've added our logo and an image for use. This only concerns the design of the label on the front of the bottle.

Label dimensions:
Label 1 (500ml bottle with spray): width 58mm x height 115mm
Label 2: (1L bottle): width 73mm x height 140mm
The design must be consistent for both bottles which you find in the pictures.

The bottles to be labeled are white. See the attachment for a photo of the bottles.

The photo must also appear on the label to identify the product's intended use.

Product information:
Brand: Voralux
Product: Sanitary Cleaner

This text must be placed on the label:
"Cleans, descales & freshens. followed with this text: "Ideal for quick and powerful cleaning. A ready-to-use product for everyday use."

- Mention the seperate USP's: Sanitary, Bathroom, Toilet, Wet areas

Appearance: This is a consumer product, but it must have a professional appearance. We would like to see a design that use the color blue from our logo.

Target Market(s)

Consumers who take care of their homes and want to maintain it the correct (professional) way

Font styles to use
Sans Serif

Colors
0054AA
0677BA
7BADD7
CADEEF
E8F1F8

Requirements
Must have
• USP's + use of image and logo + blend in 1 design
Nice to have
• Keep the color of the logo in the design
Should not have
• Comic sans

```html
<!DOCTYPE html>
<html lang="en">
<head>
<meta charset="utf-8">
<title>Voralux Sanitary Cleaner – Front Labels</title>
<link rel="stylesheet" href="https://fonts.googleapis.com/css2?family=Saira+Condensed:wght@400;500;700;800;900&family=Saira:wght@600&display=swap">
<style>
  :root {
    --blue-deep: #0054aa;
    --blue-mid: #0677ba;
    --blue-bright: #2a8ee6;
    --blue-sky: #5cb3f7;
    --blue-pale: #a8dbff;
    --blue-mist: #cadeef;
    --white-ice: #e8f1f8;
    --silver: #dfe4e9;
    --ink: #16181c;
    --page: #ffffff;
  }
  * { margin: 0; padding: 0; box-sizing: border-box; }
  html, body { width: 848px; height: 1200px; overflow: hidden; background: var(--page); }
  .canvas { position: relative; width: 848px; height: 1200px; }

  .label {
    position: absolute;
    top: 317px;
    width: 23.3em;
    overflow: hidden;
    display: flex;
    flex-direction: column;
    align-items: center;
    text-align: center;
    background: radial-gradient(ellipse 90% 55% at 50% 12%, var(--blue-pale) 0%, #86c9fb 45%, var(--blue-sky) 100%);
    font-family: "Saira Condensed", sans-serif;
  }
  .label--500ml { left: 98px; font-size: 10px; height: 46.4em; }
  .label--1l { left: 465px; font-size: 12.66px; height: 44.7em; }

  .label__content {
    position: relative;
    z-index: 1;
    display: flex;
    flex-direction: column;
    align-items: center;
  }

  .brand { margin-top: 2.4em; display: flex; flex-direction: column; align-items: center; }
  .brand__dot {
    width: 5em; height: 5em; border-radius: 50%;
    background: var(--blue-mid);
  }
  .brand__name {
    margin-top: 0.2em;
    font-family: "Saira", sans-serif;
    font-weight: 600;
    font-size: 2.4em;
    line-height: 1.1;
    color: var(--ink);
  }

  .product {
    margin-top: 0.35em;
    transform: rotate(-7deg) skewX(-12deg);
    font-weight: 900;
    font-size: 4.7em;
    line-height: 0.86;
    letter-spacing: -0.01em;
    color: var(--silver);
    text-transform: uppercase;
    text-shadow:
      0.02em 0.02em 0 #b6c3cf,
      0.04em 0.04em 0 var(--blue-bright),
      0.06em 0.06em 0 var(--blue-mid),
      0.08em 0.08em 0 var(--blue-deep);
  }
  .product__line { display: block; }
  .product__line--first { margin-right: 0.55em; }
  .product__line--second { margin-left: 0.55em; }

  .claim {
    margin-top: 0.5em;
    font-weight: 800;
    font-size: 2.1em;
    line-height: 1.1;
    letter-spacing: 0.03em;
    color: var(--white-ice);
    text-transform: uppercase;
    text-shadow: 0 0 0.06em var(--blue-mid), 0.04em 0.05em 0 var(--blue-mid);
  }
  .description {
    margin-top: 0.3em;
    font-weight: 500;
    font-size: 1.15em;
    line-height: 1.2;
    color: var(--white-ice);
    text-shadow: 0 0.05em 0.1em rgba(0, 84, 170, 0.6);
  }
  .usps {
    margin-top: 0.6em;
    list-style: none;
    display: flex;
    gap: 0.35em;
    font-weight: 500;
    font-size: 1.15em;
    color: var(--white-ice);
    text-transform: uppercase;
    white-space: nowrap;
    text-shadow: 0 0.05em 0.1em rgba(0, 84, 170, 0.6);
  }
  .usps li + li::before { content: "•"; margin-right: 0.35em; }

  .foam {
    position: absolute;
    left: 0; right: 0; bottom: 0;
    width: 100%;
    height: 30%;
    display: block;
  }
</style>
</head>
<body>
  <main class="canvas">
    <section class="label label--500ml" aria-label="Front label, 500 ml spray bottle">
      <div class="label__content">
        <div class="brand">
          <span class="brand__dot"></span>
          <span class="brand__name">Voralux</span>
        </div>
        <h1 class="product">
          <span class="product__line product__line--first">Sanitary</span>
          <span class="product__line product__line--second">Cleaner</span>
        </h1>
        <p class="claim">Cleans, descales<br>&amp; freshens.</p>
        <p class="description">Ideal for quick and powerful cleaning.<br>A ready-to-use product for everyday use.</p>
        <ul class="usps">
          <li>Sanitary</li><li>Bathroom</li><li>Toilet</li><li>Wet areas</li>
        </ul>
      </div>
      <svg class="foam" role="img" aria-label="Soap foam and bubbles" viewBox="0 0 100 60" preserveAspectRatio="none">
        <defs>
          <linearGradient id="foam-fill-500ml" x1="0" y1="0" x2="0" y2="1">
            <stop offset="0" stop-color="#b9dcf7"/>
            <stop offset="0.45" stop-color="#cfe5f7"/>
            <stop offset="1" stop-color="#eef6fc"/>
          </linearGradient>
        </defs>
        <path d="M0 10 C18 2 32 24 50 26 C68 28 82 6 100 0 V60 H0 Z" fill="url(#foam-fill-500ml)"/>
      </svg>
    </section>

    <section class="label label--1l" aria-label="Front label, 1 litre bottle">
      <div class="label__content">
        <div class="brand">
          <span class="brand__dot"></span>
          <span class="brand__name">Voralux</span>
        </div>
        <h2 class="product">
          <span class="product__line product__line--first">Sanitary</span>
          <span class="product__line product__line--second">Cleaner</span>
        </h2>
        <p class="claim">Cleans, descales<br>&amp; freshens.</p>
        <p class="description">Ideal for quick and powerful cleaning.<br>A ready-to-use product for everyday use.</p>
        <ul class="usps">
          <li>Sanitary</li><li>Bathroom</li><li>Toilet</li><li>Wet areas</li>
        </ul>
      </div>
      <svg class="foam" role="img" aria-label="Soap foam and bubbles" viewBox="0 0 100 60" preserveAspectRatio="none">
        <defs>
          <linearGradient id="foam-fill-1l" x1="0" y1="0" x2="0" y2="1">
            <stop offset="0" stop-color="#b9dcf7"/>
            <stop offset="0.45" stop-color="#cfe5f7"/>
            <stop offset="1" stop-color="#eef6fc"/>
          </linearGradient>
        </defs>
        <path d="M0 10 C18 2 32 24 50 26 C68 28 82 6 100 0 V60 H0 Z" fill="url(#foam-fill-1l)"/>
      </svg>
    </section>
  </main>
</body>
</html>
```